Business card design needed

see my website

www.aldermoorandpike.com

I am after a new logo and business card needs to fit in with the website. I like the look of typewriter text - would like this on the website as well if I could!

Industry/Entity Type

Business

Contact Information for Business Card

Aldermoor and Pike
Design and Heritage Consultants

Marisa Oakton
Principal

+61 407 963 215
marisa@aldermoorandpike.com

www.aldermoorandpike.com

back of card

Interior Design
Consultancy on Period Home restoration and renovation
Heritage Impact Statements
Conservation Management Plans
Materials Conservation
Historical Research

```html
<!DOCTYPE html>
<html lang="en">
<head>
<meta charset="utf-8">
<title>Aldermoor and Pike — Business Card</title>
<link rel="stylesheet" href="https://fonts.googleapis.com/css2?family=Courier+Prime:wght@400;700&family=Cutive&display=swap">
<style>
  :root {
    --page-bg: #e6e4e0;
    --card-white: #ffffff;
    --teal: #19a89b;
    --ink-grey: #5a5a5a;
    --ink-dark: #1f1a15;
    --photo-dark: #3e3024;
    --photo-mid: #8a6f52;
    --photo-light: #c9b394;
    --parchment-light: #e9dcb8;
    --parchment-mid: #d8c59a;
    --parchment-edge: #9c8460;
  }
  * { box-sizing: border-box; margin: 0; padding: 0; }
  html, body {
    width: 1200px;
    height: 900px;
    overflow: hidden;
    background: var(--page-bg);
  }
  .canvas {
    position: relative;
    width: 1200px;
    height: 900px;
  }
  .card {
    position: absolute;
    top: 292px;
    width: 513px;
    height: 315px;
    border-radius: 20px;
    overflow: hidden;
    box-shadow: 0 2px 8px rgba(0,0,0,0.18);
  }
  .card--front { left: 73px; background: var(--card-white); }
  .card--back  { left: 615px; }

  .brand-name {
    position: absolute;
    left: 27px;
    top: 25px;
    font-family: "Courier Prime", monospace;
    font-weight: 700;
    font-size: 36px;
    line-height: 40px;
    letter-spacing: -1.2px;
    color: var(--teal);
    white-space: nowrap;
  }
  .brand-tagline {
    position: absolute;
    left: 28px;
    top: 68px;
    width: 200px;
    font-family: "Cutive", serif;
    font-size: 14.5px;
    line-height: 18px;
    color: var(--ink-grey);
  }
  .person-name {
    position: absolute;
    left: 27px;
    top: 166px;
    font-family: "Cutive", serif;
    font-size: 22px;
    line-height: 26px;
    color: var(--teal);
    white-space: nowrap;
  }
  .person-role {
    position: absolute;
    left: 28px;
    top: 196px;
    font-family: "Cutive", serif;
    font-size: 14.5px;
    line-height: 18px;
    color: var(--ink-grey);
  }
  .contact-list {
    position: absolute;
    left: 28px;
    top: 242px;
    width: 206px;
    list-style: none;
    font-family: "Cutive", serif;
    font-size: 11px;
    line-height: 15px;
    letter-spacing: -0.3px;
    color: var(--ink-grey);
    white-space: nowrap;
  }
  .interior-photo {
    position: absolute;
    left: 243px;
    top: 108px;
    width: 248px;
    height: 184px;
    border-bottom-right-radius: 20px;
    background:
      radial-gradient(ellipse at 35% 20%, rgba(255,255,255,0.35) 0%, rgba(255,255,255,0) 30%),
      linear-gradient(135deg, var(--photo-dark) 0%, var(--photo-mid) 45%, var(--photo-light) 70%, var(--photo-mid) 100%);
  }

  .parchment {
    position: absolute;
    inset: 0;
    background:
      radial-gradient(ellipse at 45% 45%, rgba(255,255,255,0) 40%, rgba(90,65,35,0.45) 100%),
      linear-gradient(160deg, var(--parchment-mid) 0%, var(--parchment-light) 40%, var(--parchment-mid) 75%, var(--parchment-edge) 100%);
  }
  .service-list {
    position: absolute;
    left: 57px;
    top: 74px;
    list-style: none;
    font-family: "Courier Prime", monospace;
    font-weight: 700;
    font-size: 15px;
    line-height: 17.5px;
    color: var(--ink-dark);
  }
  .service-list li { margin-bottom: 9px; }
  .service-list li.wrap { width: 260px; }
</style>
</head>
<body>
<main class="canvas">
  <section class="card card--front" aria-label="Business card front">
    <h1 class="brand-name">Aldermoor and Pike</h1>
    <p class="brand-tagline">Design and Heritage Consultants</p>
    <p class="person-name">Marisa Oakton</p>
    <p class="person-role">Principal</p>
    <ul class="contact-list">
      <li>+61 407 963 215</li>
      <li>marisa@aldermoorandpike.com</li>
      <li>www.aldermoorandpike.com</li>
    </ul>
    <div class="interior-photo" role="img" aria-label="Photograph of a weathered period home interior with timber doors, a staircase and a pendant light"></div>
  </section>

  <section class="card card--back" aria-label="Business card back">
    <div class="parchment" role="img" aria-label="Aged, stained parchment paper texture"></div>
    <ul class="service-list">
      <li>Interior Design</li>
      <li class="wrap">Consultancy on Period Home restoration and renovation</li>
      <li>Heritage Impact Statements</li>
      <li>Conservation Management Plans</li>
      <li>Materials Conservation</li>
      <li>Historical Research</li>
    </ul>
  </section>
</main>
</body>
</html>
```